Clean, professional business cards for successful realtor

I want a clean and professional business card designed that successfully brands myself.
I want to be able to change the headshot, if possible. A white background instead of the brick would be great!
Please put this quote on the back of the card under the kov logo, "Ask me about my Step-Ahead program!"

Target Market(s)

Home buyers and sellers

Industry/Entity Type

Real Estate Agent

Contact Information for Business Card

Professional and Clean.

Font styles to use
Serif
Decorative
Script

Requirements
Must have
• Marlene Quist - Realtor
• Direct: 555.304.2296
• MarlSellsSA@postvane.com
• www.marlenequist.sa.kovrealty.com
Nice to have
• Lighter colors, white and crisp would be nice.
• I would prefer my photo on the front of the card

```html
<!DOCTYPE html>
<html lang="en">
<head>
<meta charset="utf-8">
<title>Marlene Quist – Realtor Business Card</title>
<link rel="stylesheet" href="https://fonts.googleapis.com/css2?family=Kaushan+Script&family=Montserrat:wght@300;400;600&display=swap">
<style>
  :root {
    --teal: #049cb0;
    --ink: #2b2b2b;
    --navy: #1d3a8a;
    --paper: #ffffff;
    --backdrop: #d4d4d4;
  }
  html, body {
    margin: 0;
    width: 1200px;
    height: 1200px;
    overflow: hidden;
    background: var(--backdrop);
  }
  .stage {
    position: relative;
    width: 1200px;
    height: 1200px;
  }
  .card {
    position: absolute;
    top: 197px;
    width: 460px;
    height: 805px;
    overflow: hidden;
    box-shadow: 0 6px 18px rgba(0,0,0,0.15);
  }
  .card--front { left: 110px; background: var(--paper); }
  .card--back  { left: 630px; background: var(--teal); }

  .front__band {
    position: absolute;
    inset: 0 0 auto 0;
    height: 270px;
    background: var(--teal);
  }
  .front__photo {
    position: absolute;
    top: 170px;
    left: 50%;
    width: 200px;
    height: 200px;
    margin-left: -100px;
    border-radius: 50%;
    border: 5px solid var(--paper);
    box-sizing: border-box;
    background: radial-gradient(circle at 50% 40%, #f4f1ee 0%, #e2cfc4 55%, #8a6a5c 100%);
  }
  .front__name {
    position: absolute;
    top: 405px;
    width: 100%;
    text-align: center;
    font-family: "Kaushan Script", cursive;
    font-weight: 400;
    font-size: 58px;
    color: var(--ink);
    margin: 0;
  }
  .front__title {
    position: absolute;
    top: 492px;
    width: 100%;
    text-align: center;
    font-family: "Montserrat", sans-serif;
    font-weight: 400;
    font-size: 20px;
    letter-spacing: 1px;
    color: var(--ink);
    margin: 0;
  }
  .contact {
    position: absolute;
    top: 558px;
    left: 58px;
    margin: 0;
    padding: 0;
    list-style: none;
    font-family: "Montserrat", sans-serif;
    font-weight: 300;
    font-size: 18px;
    color: var(--ink);
  }
  .contact__item {
    display: flex;
    align-items: center;
    gap: 16px;
    height: 36px;
  }
  .contact__icon { width: 20px; height: 20px; fill: var(--ink); flex: none; }
  .brand {
    position: absolute;
    top: 706px;
    width: 100%;
    display: flex;
    justify-content: center;
    align-items: center;
    gap: 10px;
    font-family: "Montserrat", sans-serif;
    font-weight: 600;
    font-size: 36px;
    color: var(--navy);
  }
  .brand__dot {
    width: 30px;
    height: 30px;
    border-radius: 50%;
    background: var(--navy);
  }

  .back__brand {
    position: absolute;
    top: 300px;
    width: 100%;
    display: flex;
    justify-content: center;
    align-items: center;
    gap: 10px;
    font-family: "Montserrat", sans-serif;
    font-weight: 600;
    font-size: 40px;
    color: var(--paper);
  }
  .back__brand .brand__dot { background: var(--paper); }
  .back__quote {
    position: absolute;
    top: 385px;
    left: 40px;
    right: 40px;
    margin: 0;
    text-align: center;
    font-family: "Kaushan Script", cursive;
    font-weight: 400;
    font-size: 34px;
    line-height: 1.3;
    color: var(--paper);
  }
</style>
</head>
<body>
<main class="stage">
  <section class="card card--front" aria-label="Business card front">
    <div class="front__band"></div>
    <div class="front__photo" role="img" aria-label="Headshot of Marlene Quist on a white background"></div>
    <h1 class="front__name">Marlene Quist</h1>
    <p class="front__title">REALTOR</p>
    <ul class="contact">
      <li class="contact__item">
        <svg class="contact__icon" viewBox="0 0 24 24" aria-hidden="true"><path d="M6.6 10.8a15.1 15.1 0 0 0 6.6 6.6l2.2-2.2a1 1 0 0 1 1-.25 11.4 11.4 0 0 0 3.6.57 1 1 0 0 1 1 1V20a1 1 0 0 1-1 1A17 17 0 0 1 3 4a1 1 0 0 1 1-1h3.5a1 1 0 0 1 1 1c0 1.25.2 2.45.57 3.57a1 1 0 0 1-.25 1z"/></svg>
        <span>555.304.2296</span>
      </li>
      <li class="contact__item">
        <svg class="contact__icon" viewBox="0 0 24 24" aria-hidden="true"><path d="M2 5h20v14H2z M3.5 6.5 12 13l8.5-6.5z" fill-rule="evenodd"/></svg>
        <span>MarlSellsSA@postvane.com</span>
      </li>
      <li class="contact__item">
        <svg class="contact__icon" viewBox="0 0 24 24" aria-hidden="true"><path d="M12 2a10 10 0 1 0 0 20 10 10 0 0 0 0-20zm0 1.8c.9 0 2.2 1.7 2.8 5.2H9.2c.6-3.5 1.9-5.2 2.8-5.2zM9 11h6a20 20 0 0 1 0 2H9a20 20 0 0 1 0-2zm-1.9 0a22 22 0 0 0 0 2H3.9a8 8 0 0 1 0-2zm9.8 0h3.2a8 8 0 0 1 0 2h-3.2a22 22 0 0 0 0-2zM9.2 15h5.6c-.6 3.5-1.9 5.2-2.8 5.2s-2.2-1.7-2.8-5.2zM4.6 9a8.2 8.2 0 0 1 4.3-4.4A13 13 0 0 0 7.3 9zm10.5-4.4A8.2 8.2 0 0 1 19.4 9h-2.7a13 13 0 0 0-1.6-4.4zM4.6 15h2.7a13 13 0 0 0 1.6 4.4A8.2 8.2 0 0 1 4.6 15zm12.1 0h2.7a8.2 8.2 0 0 1-4.3 4.4 13 13 0 0 0 1.6-4.4z"/></svg>
        <span>www.marlenequist.sa.kovrealty.com</span>
      </li>
    </ul>
    <div class="brand">
      <span class="brand__dot"></span>
      <span class="brand__name">kov realty</span>
    </div>
  </section>

  <section class="card card--back" aria-label="Business card back">
    <div class="back__brand">
      <span class="brand__dot"></span>
      <span class="brand__name">kov realty</span>
    </div>
    <p class="back__quote">“Ask me about my Step-Ahead program!”</p>
  </section>
</main>
</body>
</html>
```